I want a business letter head designed, one that I can have printed but also one that I can use as an insert for proforma documentation that is printed in house.

Business name : RJ Penfold & Associates
Address: PO Box 738
Tewantin Qld 4587

Type of business: Accounting practice- accounting, taxation, audit, self managed superannuation,

Colour scheme: black and blue - previously designed a business card; however the blue that is one the cards is very washed out and I am not particularly happy with it.

Industry/Entity Type

Business

```html
<!DOCTYPE html>
<html lang="en">
<head>
<meta charset="utf-8">
<title>RJ Penfold &amp; Associates – Letterhead</title>
<link rel="stylesheet" href="https://fonts.googleapis.com/css2?family=Arimo:wght@400&family=Tinos:wght@400&display=swap">
<style>
  :root {
    --backdrop: #e8ecf0;
    --paper: #ffffff;
    --ink: #000000;
    --brand-blue: #1e90f0;
    --watermark-blue: #b9e0fb;
  }
  * { margin: 0; padding: 0; box-sizing: border-box; }
  html, body {
    width: 1200px;
    height: 1013px;
    overflow: hidden;
    background: var(--backdrop);
  }
  .letterhead {
    position: absolute;
    left: 270px;
    top: 36px;
    width: 660px;
    height: 940px;
    background: var(--paper);
    overflow: hidden;
    box-shadow: 0 6px 24px rgba(0, 0, 0, 0.12);
  }
  .side-band {
    position: absolute;
    left: 0;
    top: 0;
    width: 91px;
    height: 100%;
    background: var(--ink);
  }
  .brand {
    position: absolute;
    left: 18px;
    top: 24px;
    display: flex;
    align-items: center;
    gap: 14px;
  }
  .brand-square {
    width: 44px;
    height: 44px;
    background: var(--brand-blue);
    flex: none;
  }
  .brand-name {
    font-family: "Tinos", "Times New Roman", serif;
    font-size: 22px;
    line-height: 21px;
    color: var(--ink);
    margin-left: 14px;
  }
  .contact {
    position: absolute;
    right: 21px;
    top: 35px;
    text-align: right;
    font-family: "Arimo", Arial, sans-serif;
    font-size: 11.5px;
    line-height: 16px;
    color: var(--ink);
  }
  .services { word-spacing: 1px; }
  .corner-mark {
    position: absolute;
    right: -10px;
    bottom: -10px;
    width: 220px;
    height: 210px;
    background: var(--watermark-blue);
  }
</style>
</head>
<body>
  <main class="letterhead">
    <div class="side-band"></div>

    <header class="brand">
      <div class="brand-square"></div>
      <h1 class="brand-name" style="font-weight:400">RJ Penfold<br>&amp; Associates.</h1>
    </header>

    <address class="contact" style="font-style:normal">
      <p class="services">Accounting &nbsp;. Taxation &nbsp;. Audit &nbsp;. Self Managed &nbsp;. Superannuation</p>
      <p>PO Box 738 Tewantin Qld 4587</p>
      <p>email: office@rjpenfoldassociates.com.au</p>
    </address>

    <div class="corner-mark"></div>
  </main>
</body>
</html>
```